Brand New Luxury Dog Kennel Needs a Flyer Design

We need a flyer design for a new type of dog kennel in Derbyshire (UK). We are trying to separate ourselves from the original kennel types and offer a more hotel orientated approach with much better facilities, massive rooms, large play areas (indoors and out (across the farm land)), 24/7 web cam access for the owners, etc.
The name of the company is Cat and Ladle, it's based on a farm called Brambleton Farm.
We have started a website (not complete yet), but you can get an idea of style there; http://www.catandladle-example.co.uk/
The final design should emphasise that we are different from the other kennels, we're very professional and caring. It's very much the dogs holiday.
Size of Flyer should be around 216 x 139 mm

```html
<!DOCTYPE html>
<html lang="en">
<head>
<meta charset="utf-8">
<title>Cat &amp; Ladle – Hotel Rooms for Dogs</title>
<link href="https://fonts.googleapis.com/css2?family=Fjalla+One&family=Lobster+Two:ital,wght@1,700&family=Signika:wght@400;600;700&display=swap" rel="stylesheet">
<style>
  :root {
    --page-bg: #ecebe7;
    --flyer-brown: #5f4128;
    --flyer-brown-dark: #4b321e;
    --flyer-edge: #f3f1ec;
    --gold: #f0bd4a;
    --cream: #f4efe3;
    --cream-shade: #d9d1bf;
    --ink-brown: #5a3b22;
    --white: #ffffff;
    --muted: #8a7a66;
  }
  * { box-sizing: border-box; margin: 0; padding: 0; }
  html, body { width: 1200px; height: 900px; overflow: hidden; }
  body { background: var(--page-bg); position: relative; font-family: "Signika", sans-serif; }

  .flyer {
    position: absolute; left: 375px; top: 45px; width: 450px; height: 810px;
    background: linear-gradient(180deg, var(--flyer-brown) 0%, var(--flyer-brown-dark) 100%);
    border: 8px solid var(--flyer-edge);
    box-shadow: 0 10px 30px rgba(0,0,0,.25);
    color: var(--white);
  }

  .brand-tab { position: absolute; left: 95px; top: -8px; width: 245px; height: 140px; }
  .brand-tab svg { position: absolute; inset: 0; }
  .brand-name {
    position: absolute; top: 30px; width: 100%; text-align: center;
    font-family: "Signika", sans-serif; font-weight: 600; font-size: 28px; color: var(--ink-brown);
  }
  .brand-tagline {
    position: absolute; top: 80px; width: 100%; text-align: center;
    font-size: 13px; color: var(--muted);
  }

  .ornament {
    position: absolute; left: 195px; top: 150px; width: 44px; height: 18px;
    background: var(--cream); opacity: .85; border-radius: 22px 22px 4px 4px;
  }
  .rule { position: absolute; left: 60px; top: 176px; width: 315px; height: 1px; background: rgba(255,255,255,.45); }

  .headline {
    position: absolute; top: 192px; width: 100%; text-align: center;
    font-family: "Fjalla One", sans-serif; font-size: 52px; letter-spacing: 1px;
    color: var(--gold); text-shadow: 2px 3px 0 rgba(0,0,0,.35);
  }
  .headline-sub {
    position: absolute; top: 258px; width: 100%; text-align: center;
    font-family: "Lobster Two", cursive; font-style: italic; font-weight: 700; font-size: 34px;
    color: var(--cream);
  }

  .ribbon { position: absolute; left: 26px; top: 318px; width: 384px; height: 200px; }
  .ribbon svg { position: absolute; inset: 0; }
  .ribbon-text {
    position: absolute; width: 100%; text-align: center; color: var(--ink-brown);
    font-family: "Signika", sans-serif; font-weight: 700; text-transform: uppercase; white-space: nowrap;
  }
  .ribbon-opening { top: 24px; font-size: 25px; letter-spacing: .5px; }
  .ribbon-on { top: 60px; font-family: "Lobster Two", cursive; font-style: italic; text-transform: none; font-size: 24px; }
  .ribbon-farm { top: 116px; font-size: 31px; letter-spacing: .5px; }

  .features { position: absolute; left: 62px; top: 548px; list-style: none; }
  .features li {
    display: flex; align-items: center; height: 32px; margin-bottom: 4px;
    font-weight: 600; font-size: 17px; letter-spacing: .5px; text-transform: uppercase; white-space: nowrap;
  }
  .features li:nth-child(2) { margin-left: -8px; }
  .features li:nth-child(3) { margin-left: -16px; }
  .features li:nth-child(4) { margin-left: -24px; }
  .tick { width: 26px; height: 22px; margin-right: 8px; flex: none; }

  .social { position: absolute; left: 20px; right: 20px; bottom: 22px; display: flex; justify-content: space-between; }
  .social-item { display: flex; align-items: center; gap: 7px; font-size: 10px; font-weight: 700; color: var(--cream); white-space: nowrap; }
  .social-item:last-child { margin-top: 14px; }
  .social-dot { width: 26px; height: 26px; border-radius: 50%; background: var(--cream); flex: none; }
</style>
</head>
<body>
  <article class="flyer">
    <header class="brand-tab">
      <svg viewBox="0 0 245 140" width="245" height="140" aria-hidden="true">
        <polygon points="0,0 245,0 245,112 122,140 0,112" fill="var(--cream)"/>
        <polygon points="0,112 122,140 245,112 245,118 122,140 0,118" fill="var(--cream-shade)"/>
      </svg>
      <div class="brand-name">Cat &amp; Ladle</div>
      <div class="brand-tagline">Country stays for well-loved pets</div>
    </header>

    <div class="ornament" role="img" aria-label="Small decorative flourish"></div>
    <div class="rule"></div>

    <h1 class="headline">HOTEL ROOMS</h1>
    <p class="headline-sub">for dogs</p>

    <section class="ribbon">
      <svg viewBox="0 0 384 200" width="384" height="200" aria-hidden="true">
        <polygon points="8,4 376,14 360,60 372,98 14,92" fill="var(--cream)"/>
        <polygon points="40,98 350,100 340,122 372,190 18,184 36,140" fill="rgba(0,0,0,.25)"/>
        <polygon points="24,100 360,100 348,146 366,186 12,180 30,140" fill="var(--cream)"/>
      </svg>
      <div class="ribbon-text ribbon-opening">Opening Autumn 2014</div>
      <div class="ribbon-text ribbon-on">On</div>
      <div class="ribbon-text ribbon-farm">Brambleton Farm</div>
    </section>

    <ul class="features">
      <li><svg class="tick" viewBox="0 0 26 22"><path d="M2 12 L10 19 L24 2" fill="none" stroke="var(--gold)" stroke-width="3.5" stroke-linecap="round" stroke-linejoin="round"/></svg>Better facilities</li>
      <li><svg class="tick" viewBox="0 0 26 22"><path d="M2 12 L10 19 L24 2" fill="none" stroke="var(--gold)" stroke-width="3.5" stroke-linecap="round" stroke-linejoin="round"/></svg>Massive rooms</li>
      <li><svg class="tick" viewBox="0 0 26 22"><path d="M2 12 L10 19 L24 2" fill="none" stroke="var(--gold)" stroke-width="3.5" stroke-linecap="round" stroke-linejoin="round"/></svg>Large play areas</li>
      <li><svg class="tick" viewBox="0 0 26 22"><path d="M2 12 L10 19 L24 2" fill="none" stroke="var(--gold)" stroke-width="3.5" stroke-linecap="round" stroke-linejoin="round"/></svg>24/7 cam access to owners</li>
    </ul>

    <footer class="social">
      <div class="social-item"><span class="social-dot"></span>social-example.com/catandladle</div>
      <div class="social-item"><span class="social-dot"></span>chirp-example.com/catandladle</div>
    </footer>
  </article>
</body>
</html>
```